CRPG is needing business cards, and stationary created.

Pixel Forge created a logo for our business, and now we are wanting business cards, and stationary. I have included two designs of the same logo. Please feel free to use them as you want. The name of the company is Cedar Ridge Property Group LLC, the address is 812 NE Willow Ln., Suite 9, the city & state is Bend, Oregon, zip code is 97815, Telephone number is 541-327-4489, Fax number is 541-327-6051, the name on the business card is Carl Whitby CMCA

Industry/Entity Type

Property Management

Contact Information for Business Card

The card needs to look professional. Upscale.

Requirements
Must have
• The colors we are using are on the logo that has been uploaded.

```html
<!DOCTYPE html>
<html lang="en">
<head>
<meta charset="utf-8">
<title>Cedar Ridge Property Group – Business Cards</title>
<link href="https://fonts.googleapis.com/css2?family=Open+Sans:wght@400;600;700&display=swap" rel="stylesheet">
<style>
  :root {
    --teal: #1a8c7a;
    --teal-pale: #e6f2ef;
    --ink: #3a3a3a;
    --white: #ffffff;
    --backdrop: #cfcfcf;
  }
  html, body {
    margin: 0;
    padding: 0;
    width: 1200px;
    height: 900px;
    overflow: hidden;
    background: var(--backdrop);
    font-family: "Open Sans", Arial, sans-serif;
  }
  .stage {
    position: relative;
    width: 1200px;
    height: 900px;
  }
  .card {
    position: absolute;
    width: 525px;
    height: 300px;
    border-radius: 26px;
    overflow: hidden;
    box-shadow: 0 10px 24px rgba(0,0,0,0.18);
  }
  .card-front {
    left: 50px;
    top: 150px;
    background: var(--teal);
    display: flex;
    align-items: center;
    justify-content: center;
  }
  .card-back {
    left: 625px;
    top: 450px;
    background: var(--white);
  }
  .wordmark {
    display: flex;
    align-items: center;
    gap: 14px;
    font-weight: 700;
    letter-spacing: 0.04em;
    text-transform: uppercase;
    line-height: 1.05;
  }
  .wordmark-mark {
    width: 34px;
    height: 34px;
    flex: none;
  }
  .card-front .wordmark { color: var(--white); font-size: 26px; }
  .card-front .wordmark-mark { background: var(--white); }
  .card-back .wordmark {
    position: absolute;
    left: 34px;
    top: 70px;
    color: var(--teal);
    font-size: 20px;
  }
  .card-back .wordmark-mark { background: var(--teal); width: 30px; height: 30px; }
  .backdrop-block {
    position: absolute;
    right: 30px;
    top: -20px;
    width: 210px;
    height: 190px;
    background: var(--teal-pale);
  }
  .address {
    position: absolute;
    right: 34px;
    top: 176px;
    text-align: right;
    color: var(--ink);
    font-size: 13px;
    line-height: 1.35;
  }
  .holder {
    position: absolute;
    left: 34px;
    top: 186px;
    font-size: 17px;
    letter-spacing: 0.05em;
    color: var(--teal);
    text-transform: uppercase;
  }
  .holder .credential {
    color: var(--ink);
    font-size: 12px;
    margin-left: 4px;
  }
  .contacts {
    position: absolute;
    left: 34px;
    top: 222px;
    margin: 0;
    padding: 0;
    list-style: none;
    font-size: 14px;
    color: var(--ink);
    line-height: 1.35;
  }
  .contacts li { display: flex; align-items: center; gap: 6px; }
  .contacts svg { width: 12px; height: 12px; fill: var(--teal); }
  .card-band {
    position: absolute;
    left: 0;
    right: 0;
    bottom: 0;
    height: 12px;
    background: var(--teal);
  }
</style>
</head>
<body>
<main class="stage">
  <section class="card card-front" aria-label="Business card front">
    <div class="wordmark">
      <span class="wordmark-mark"></span>
      <span>Cedar Ridge<br>Property Group</span>
    </div>
  </section>

  <section class="card card-back" aria-label="Business card back">
    <div class="backdrop-block"></div>
    <div class="wordmark">
      <span class="wordmark-mark"></span>
      <span>Cedar Ridge<br>Property Group</span>
    </div>
    <address class="address">812 NE Willow Ln., Suite 9<br>Bend, Oregon, 97815</address>
    <div class="holder">Carl Whitby<span class="credential">CMCA</span></div>
    <ul class="contacts">
      <li>
        <svg viewBox="0 0 24 24" aria-hidden="true"><path d="M6.6 10.8a15.1 15.1 0 0 0 6.6 6.6l2.2-2.2a1 1 0 0 1 1-.25 11.4 11.4 0 0 0 3.6.57 1 1 0 0 1 1 1V20a1 1 0 0 1-1 1A17 17 0 0 1 3 4a1 1 0 0 1 1-1h3.5a1 1 0 0 1 1 1c0 1.25.2 2.45.57 3.6a1 1 0 0 1-.25 1z"/></svg>
        541-327-4489
      </li>
      <li>
        <svg viewBox="0 0 24 24" aria-hidden="true"><path d="M6 3h9l3 3v4H6zM4 11h16a2 2 0 0 1 2 2v6h-4v2H6v-2H2v-6a2 2 0 0 1 2-2zm4 5v3h8v-3z"/></svg>
        541-327-6051
      </li>
    </ul>
    <div class="card-band"></div>
  </section>
</main>
</body>
</html>
```